Cover design for new academic journal on deconstruction and psychoanalysis

We need a cover for a new academic journal on deconstruction and psychoanalysis. The name of the journal is "The Liminal Remainder: A Journal of Deconstruction and Psychoanalysis" (LR) and it is published by the Calloway Ridge University Press(CRP).

Here is a description of the journal on the CRP website:

http://www.callowayridgepress.example.edu/product/The-Liminal-Remainder,482917.aspx

We are looking for a design that is more abstract and does not have icons or photographs of people, especially not photos of Valmont or Kessler. The design should be contemporary with clean lines and simple fonts. Again, it should be abstract, with no icons or iconography.

The cover should simply have the full name of the journal and then "Volume 1, Issue 1, 2014" on the cover and "Vol. 1, No. 1, 2014" on the spine.

Attached you can see some ideas that we rejected from CRP. It is important that you understand that these designs were rejected and are just being offered as examples of what the cover will look like in general, as a template of sorts.

The cover should have a bold abstract design, with a space for the title and "Volume 1, Issue 1, 2014."

Something bold and contemporary.

Academics, scholars and psychoanalysts.

University

Sans Serif

• Must be abstract, bold, have color, and must be contemporary.
• No icons, no photographs of Valmont, Kessler, or anyone.

```html
<!DOCTYPE html>
<html lang="en">
<head>
<meta charset="utf-8">
<title>The Liminal Remainder — Cover</title>
<link rel="stylesheet" href="https://fonts.googleapis.com/css2?family=Arimo:ital,wght@0,400;0,700;1,400;1,700&display=swap">
<style>
  :root {
    --crimson: #8a0f12;
    --blood: #5c0709;
    --ember: #b0161a;
    --ink: #070203;
    --paper: #f2f0ee;
  }
  html, body {
    margin: 0;
    padding: 0;
    width: 1200px;
    height: 900px;
    overflow: hidden;
    background: var(--ink);
  }
  .cover {
    position: relative;
    width: 1200px;
    height: 900px;
    overflow: hidden;
    font-family: "Arimo", Arial, sans-serif;
    color: var(--paper);
  }
  .cover__artwork {
    position: absolute;
    inset: 0;
    background:
      radial-gradient(ellipse 260px 200px at 130px 150px, var(--ember) 0%, transparent 70%),
      radial-gradient(ellipse 300px 240px at 400px 420px, var(--crimson) 0%, transparent 72%),
      radial-gradient(ellipse 220px 260px at 120px 700px, var(--blood) 0%, transparent 70%),
      radial-gradient(ellipse 320px 200px at 900px 120px, var(--crimson) 0%, transparent 70%),
      radial-gradient(ellipse 280px 220px at 1050px 760px, var(--crimson) 0%, transparent 72%),
      radial-gradient(ellipse 360px 120px at 820px 620px, var(--ink) 0%, transparent 80%),
      radial-gradient(ellipse 200px 300px at 520px 600px, var(--ink) 0%, transparent 75%),
      linear-gradient(135deg, var(--blood) 0%, #2a0405 45%, var(--blood) 70%, #240304 100%);
  }
  .spine__title,
  .spine__issue {
    position: absolute;
    writing-mode: vertical-rl;
    white-space: nowrap;
    text-shadow: 1px 1px 2px rgba(0,0,0,0.7);
  }
  .spine__title {
    left: 584px;
    top: 52px;
    font-size: 29px;
    font-weight: 700;
    letter-spacing: 1px;
  }
  .spine__issue {
    left: 590px;
    top: 700px;
    font-size: 18px;
    font-weight: 700;
    letter-spacing: 1.5px;
  }
  .front__title {
    position: absolute;
    left: 690px;
    top: 148px;
    margin: 0;
    font-weight: 700;
    font-size: 126px;
    line-height: 130px;
    letter-spacing: 6px;
    white-space: nowrap;
    transform: scaleX(0.56);
    transform-origin: left top;
    text-shadow: 4px 3px 4px rgba(0,0,0,0.8);
  }
  .front__title span { display: block; }
  .front__subtitle {
    position: absolute;
    left: 692px;
    top: 588px;
    margin: 0;
    font-style: italic;
    font-weight: 700;
    font-size: 22px;
    line-height: 56px;
    letter-spacing: 3px;
    text-shadow: 1px 1px 2px rgba(0,0,0,0.7);
  }
  .front__issue {
    position: absolute;
    left: 692px;
    top: 852px;
    margin: 0;
    font-size: 20px;
    font-weight: 700;
    letter-spacing: 2.5px;
    text-shadow: 1px 1px 2px rgba(0,0,0,0.7);
  }
</style>
</head>
<body>
  <main class="cover">
    <div class="cover__artwork" role="img" aria-label="Abstract painted texture in deep crimson and black covering the whole wrap"></div>

    <div class="spine__title">The Liminal Remainder</div>
    <div class="spine__issue">Vol. 1, No. 1, 2014</div>

    <h1 class="front__title">
      <span>THE</span>
      <span>LIMINAL</span>
      <span>REMAINDER</span>
    </h1>
    <p class="front__subtitle">A Journal of Deconstruction<br>and Psychoanalysis</p>
    <p class="front__issue">Volume 1, Issue 1, 2014</p>
  </main>
</body>
</html>
```